Construction Contractor
Bayt Nuwaris
Professional
Fahad Omar Qurashi
Owner
Rawda Street P.O.Box 483920 Jeddah 24719 Saudi Arabia
baytnuwaris@mailbox-example.com
We need Logo to be in the middle and company name under the logo

```html
<!DOCTYPE html>
<html lang="en">
<head>
<meta charset="utf-8">
<title>Bayt Nuwaris Stationery</title>
<link rel="stylesheet" href="https://fonts.googleapis.com/css2?family=Montserrat:wght@400;600;700&display=swap">
<style>
  :root{
    --bg:#f1f1f0;
    --paper:#ffffff;
    --brown:#5b3b1f;
    --gold:#b69a5e;
    --ink:#6b5a4a;
    --faint:#ece7df;
    --edge:#dcdad6;
  }
  *{margin:0;padding:0;box-sizing:border-box}
  html,body{width:1200px;height:936px;overflow:hidden;background:var(--bg)}
  body{position:relative;font-family:"Montserrat",Arial,sans-serif;color:var(--ink)}
  .sheet{position:absolute;background:var(--paper);border:1px solid var(--edge);overflow:hidden}
  .band{position:absolute;left:0;bottom:0;width:100%}
  .band svg{display:block;width:100%;height:100%}
  .band-text{position:absolute;left:0;width:100%;text-align:center;color:#fff;letter-spacing:.28em;white-space:nowrap}
  .brand{display:flex;align-items:center;gap:8px;color:var(--brown);font-weight:700;letter-spacing:.04em;white-space:nowrap}
  .brand-mark{background:var(--gold);flex:none}

  .letterhead{left:183px;top:68px;width:390px;height:546px}
  .letterhead .brand{position:absolute;left:44px;top:86px;font-size:17px}
  .letterhead .brand-mark{width:12px;height:12px}
  .contact{position:absolute;left:252px;top:30px;list-style:none;font-size:6.5px;line-height:11px;color:var(--ink);white-space:nowrap}
  .contact li{display:flex;align-items:center;gap:4px}
  .contact li::before{content:"";width:5px;height:5px;background:var(--gold);border-radius:50%;flex:none}
  .watermark{position:absolute;left:0;width:100%;top:250px;text-align:center;font-size:34px;font-weight:700;color:var(--faint);letter-spacing:.06em}
  .letterhead .band{height:90px}
  .letterhead .band-text{bottom:16px;font-size:12px}

  .folder{left:634px;top:51px;width:361px;height:563px}
  .folder .brand-stack{position:absolute;left:0;width:100%;top:290px;display:flex;flex-direction:column;align-items:center;gap:12px}
  .folder .brand-mark{width:26px;height:26px}
  .folder .brand-name{font-size:30px;font-weight:700;color:var(--brown);letter-spacing:.04em;white-space:nowrap}
  .folder .band{height:70px}
  .folder .band-text{bottom:14px;font-size:11px}

  .card-front{left:43px;top:655px;width:180px;height:101px}
  .card-front .brand{position:absolute;left:12px;top:11px;font-size:9px;gap:5px}
  .card-front .brand-mark{width:7px;height:7px}
  .person{position:absolute;left:12px;top:28px;font-size:5px;line-height:7px;color:var(--ink);white-space:nowrap}
  .person strong{display:block;font-size:6px;font-weight:700;color:var(--brown)}
  .card-details{position:absolute;left:12px;top:46px;font-size:4.8px;line-height:7px;white-space:nowrap}
  .card-front .band{height:28px}

  .card-back{left:43px;top:781px;width:180px;height:107px}
  .card-back .brand{position:absolute;left:0;width:100%;top:32px;justify-content:center;font-size:12px;gap:6px}
  .card-back .brand-mark{width:9px;height:9px}
  .card-back .band{height:32px}
  .card-back .band-text{bottom:7px;font-size:6px}

  .envelope-front{left:261px;top:665px;width:419px;height:223px}
  .envelope-front .brand{position:absolute;left:32px;top:86px;font-size:14px}
  .envelope-front .brand-mark{width:10px;height:10px}
  .envelope-front .address{position:absolute;left:32px;top:108px;font-size:5.5px;color:var(--ink);white-space:nowrap}

  .envelope-back{left:736px;top:665px;width:423px;height:223px}
  .envelope-back .flap{position:absolute;left:0;top:0;width:100%;height:100%}
  .envelope-back .band-text{top:30px;color:var(--brown);font-size:11px}
</style>
</head>
<body>

<section class="sheet letterhead" aria-label="Letterhead">
  <div class="brand"><span class="brand-mark"></span>BAYT NUWARIS</div>
  <ul class="contact">
    <li>Rawda Street P.O.Box 483920</li>
    <li>Jeddah 24719 Saudi Arabia</li>
    <li>Tel +966 12 000 0000</li>
    <li>Fax +966 12 000 0001</li>
    <li>baytnuwaris@mailbox-example.com</li>
  </ul>
  <div class="watermark" aria-hidden="true">BAYT NUWARIS</div>
  <div class="band">
    <svg viewBox="0 0 390 90" preserveAspectRatio="none">
      <path d="M0 22 Q190 -4 390 28 L390 90 L0 90Z" fill="var(--gold)"/>
      <path d="M0 30 Q190 4 390 36 L390 90 L0 90Z" fill="var(--brown)"/>
    </svg>
    <div class="band-text">www.baytnuwaris.example</div>
  </div>
</section>

<section class="sheet folder" aria-label="Presentation folder">
  <div class="brand-stack">
    <span class="brand-mark"></span>
    <span class="brand-name">BAYT NUWARIS</span>
  </div>
  <div class="band">
    <svg viewBox="0 0 361 70" preserveAspectRatio="none">
      <path d="M0 14 Q180 -4 361 18 L361 70 L0 70Z" fill="var(--gold)"/>
      <path d="M0 21 Q180 3 361 25 L361 70 L0 70Z" fill="var(--brown)"/>
    </svg>
    <div class="band-text">www.baytnuwaris.example</div>
  </div>
</section>

<section class="sheet card-front" aria-label="Business card front">
  <div class="brand"><span class="brand-mark"></span>BAYT NUWARIS</div>
  <div class="person"><strong>Fahad Omar Qurashi</strong>Owner</div>
  <div class="card-details">Rawda Street P.O.Box 483920<br>Jeddah 24719 Saudi Arabia<br>baytnuwaris@mailbox-example.com</div>
  <div class="band">
    <svg viewBox="0 0 180 28" preserveAspectRatio="none">
      <path d="M0 9 Q90 -2 180 11 L180 28 L0 28Z" fill="var(--gold)"/>
      <path d="M0 13 Q90 2 180 15 L180 28 L0 28Z" fill="var(--brown)"/>
    </svg>
  </div>
</section>

<section class="sheet card-back" aria-label="Business card back">
  <div class="brand"><span class="brand-mark"></span>BAYT NUWARIS</div>
  <div class="band">
    <svg viewBox="0 0 180 32" preserveAspectRatio="none">
      <path d="M0 6 Q90 -2 180 8 L180 32 L0 32Z" fill="var(--gold)"/>
      <path d="M0 10 Q90 2 180 12 L180 32 L0 32Z" fill="var(--brown)"/>
    </svg>
    <div class="band-text">www.baytnuwaris.example</div>
  </div>
</section>

<section class="sheet envelope-front" aria-label="Envelope front">
  <div class="brand"><span class="brand-mark"></span>BAYT NUWARIS</div>
  <div class="address">Rawda Street P.O.Box 483920 Jeddah 24719 Saudi Arabia</div>
</section>

<section class="sheet envelope-back" aria-label="Envelope back">
  <svg class="flap" viewBox="0 0 423 223" preserveAspectRatio="none">
      <path d="M0 72 Q211 50 423 78 L423 223 L0 223Z" fill="var(--gold)"/>
      <path d="M0 80 Q211 58 423 86 L423 223 L0 223Z" fill="var(--brown)"/>
  </svg>
  <div class="band-text">www.baytnuwaris.example</div>
</section>

</body>
</html>
```